New Clothing Line Launch Flyer

Needing an immediate eye catching flyer to be used as promotion for our clothing company Harbor & Willow Clothing. We are a new clothing company with a mission statement of "Self-Motivation and Devotion". Needs to have a modern club style feel to it with the website www.HarborAndWillowClothing.example on it.

Target Market(s)

Male and Female 16-37 years of age.

Industry/Entity Type

Clothing

Requirements
Must have
• www.harborandwillowclothing.example
Has to grab you attention as soon as you look at it!
facebook.com/harborandwillowclothing.

```html
<!DOCTYPE html>
<html lang="en">
<head>
<meta charset="utf-8">
<title>Harbor &amp; Willow Clothing – Launch Flyer</title>
<link rel="stylesheet" href="https://fonts.googleapis.com/css2?family=Roboto+Mono:wght@400;700&family=Source+Code+Pro:wght@900&display=swap">
<style>
  :root {
    --paper: #ffffff;
    --night: #0b1214;
    --plum: #4b2e3a;
    --plum-soft: #6a4654;
    --slate: #4a4b4c;
    --white: #ffffff;
    --mist: #c6c6c6;
    --cream: #fde8cf;
  }
  html, body {
    margin: 0;
    padding: 0;
    width: 1200px;
    height: 1000px;
    overflow: hidden;
    background: var(--paper);
  }
  .flyer {
    position: relative;
    width: 1200px;
    height: 1000px;
    background: var(--paper);
    overflow: hidden;
  }
  .flyer__panel {
    position: absolute;
    left: 28px;
    top: 32px;
    width: 1139px;
    height: 933px;
    background: var(--night);
    overflow: hidden;
  }
  .flyer__splatter {
    position: absolute;
    inset: 0;
    width: 100%;
    height: 100%;
  }
  .brand-mark {
    position: absolute;
    left: 200px;
    top: 160px;
    width: 260px;
    display: flex;
    align-items: center;
    gap: 14px;
  }
  .brand-mark__dot {
    flex: none;
    width: 30px;
    height: 30px;
    border-radius: 50%;
    background: var(--white);
  }
  .brand-mark__name {
    font-family: "Roboto Mono", monospace;
    font-weight: 700;
    font-size: 24px;
    line-height: 1.15;
    color: var(--white);
    text-transform: uppercase;
    letter-spacing: 1px;
  }
  .headline {
    position: absolute;
    left: 372px;
    top: 478px;
    transform-origin: 0 0;
    transform: rotate(-45deg);
    color: var(--white);
  }
  .headline__intro {
    display: block;
    margin-left: 58px;
    font-family: "Roboto Mono", monospace;
    font-size: 22px;
    line-height: 1;
  }
  .headline__body {
    display: flex;
    align-items: stretch;
    gap: 18px;
  }
  .headline__bar,
  .motto__bar {
    flex: none;
    background: var(--white);
  }
  .headline__bar { width: 38px; margin: 8px 0 10px; }
  .headline__name {
    margin: 0;
    font-family: "Source Code Pro", monospace;
    font-weight: 900;
    font-size: 72px;
    line-height: 0.98;
    text-transform: uppercase;
    white-space: nowrap;
  }
  .motto {
    position: absolute;
    left: 718px;
    top: 478px;
    transform-origin: 0 0;
    transform: rotate(45deg);
    display: flex;
    gap: 16px;
  }
  .motto__bar { width: 34px; margin: 4px 0 6px; }
  .motto__text {
    margin: 0;
    font-family: "Source Code Pro", monospace;
    font-weight: 900;
    font-size: 46px;
    line-height: 1;
    color: var(--mist);
    text-transform: uppercase;
    white-space: nowrap;
  }
  .social {
    position: absolute;
    left: 362px;
    top: 500px;
    transform-origin: 0 0;
    transform: rotate(45deg);
    margin: 0;
    font-family: "Roboto Mono", monospace;
    font-size: 24px;
    color: var(--white);
    white-space: nowrap;
  }
</style>
</head>
<body>
  <main class="flyer">
    <div class="flyer__panel">
      <svg class="flyer__splatter" viewBox="0 0 1139 933" role="img" aria-label="Paint splatter backdrop in plum, slate grey and cream droplets">
        <defs>
          <radialGradient id="plumWash" cx="50%" cy="50%" r="50%">
            <stop offset="0" stop-color="#4b2e3a"/>
            <stop offset="0.8" stop-color="#4b2e3a"/>
            <stop offset="1" stop-color="#4b2e3a" stop-opacity="0"/>
          </radialGradient>
          <radialGradient id="slateWash" cx="50%" cy="50%" r="50%">
            <stop offset="0" stop-color="#4a4b4c" stop-opacity="0.9"/>
            <stop offset="1" stop-color="#4a4b4c" stop-opacity="0"/>
          </radialGradient>
        </defs>
        <ellipse cx="300" cy="330" rx="300" ry="80" fill="url(#slateWash)"/>
        <ellipse cx="330" cy="110" rx="130" ry="90" fill="url(#plumWash)" opacity="0.8"/>
        <ellipse cx="600" cy="440" rx="560" ry="170" fill="url(#plumWash)"/>
        <ellipse cx="470" cy="700" rx="140" ry="170" fill="url(#plumWash)"/>
      </svg>

      <div class="brand-mark">
        <span class="brand-mark__dot"></span>
        <span class="brand-mark__name">Harbor &amp; Willow<br>Clothing Co.</span>
      </div>
    </div>

    <div class="headline">
      <span class="headline__intro">introducing...</span>
      <div class="headline__body">
        <span class="headline__bar"></span>
        <h1 class="headline__name">Harbor<br>&amp; Willow<br>Clothing.example</h1>
      </div>
    </div>

    <div class="motto">
      <span class="motto__bar"></span>
      <p class="motto__text">Self-Motivation<br>and<br>Devotion</p>
    </div>

    <p class="social">fb /harbor and willow clothing</p>
  </main>
</body>
</html>
```